BRIM! Card

The single side "business card" will be utilized to write down product information for our customers. The card needs to include our logo in josefin font and read BRIM! on the front. Our brand colors are espresso brown and copper. The back needs to be white (blank) to allow us to write information down. We want modern, bold, clean and fun.
I have attached a copy of our logo but you do not have to utilize exactly as shown.

```html
<!DOCTYPE html>
<html lang="en">
<head>
<meta charset="utf-8">
<title>BRIM! Card</title>
<link href="https://fonts.googleapis.com/css2?family=Josefin+Sans:wght@400&display=swap" rel="stylesheet">
<style>
  :root {
    --espresso: #2b1812;
    --copper: #c2672b;
    --card-white: #ffffff;
    --ink: #231a17;
    --backdrop: #e9e7ec;
  }
  * { margin: 0; padding: 0; box-sizing: border-box; }
  html, body {
    width: 1200px;
    height: 900px;
    overflow: hidden;
    background: var(--backdrop);
  }
  .card-set {
    position: absolute;
    top: 307px;
    left: 70px;
    display: flex;
    gap: 60px;
  }
  .card {
    width: 500px;
    height: 286px;
    position: relative;
    box-shadow: 0 4px 10px rgba(0, 0, 0, 0.25);
  }
  .card--front {
    background: var(--espresso);
    display: flex;
    align-items: center;
    justify-content: center;
  }
  .front-name {
    font-family: "Josefin Sans", sans-serif;
    font-weight: 400;
    font-size: 64px;
    letter-spacing: 0;
    line-height: 1;
    color: var(--copper);
    margin-top: 10px;
  }
  .card--back {
    background: var(--card-white);
  }
  .brand-block {
    position: absolute;
    top: 30px;
    left: 0;
    right: 0;
    text-align: center;
    font-family: "Josefin Sans", sans-serif;
    font-weight: 400;
    color: var(--ink);
  }
  .brand-name {
    font-size: 30px;
    line-height: 1;
  }
  .brand-tagline {
    font-size: 12px;
    line-height: 1.2;
    margin-top: 6px;
  }
</style>
</head>
<body>
  <main class="card-set">
    <section class="card card--front">
      <p class="front-name">BRIM!</p>
    </section>
    <section class="card card--back">
      <div class="brand-block">
        <p class="brand-name">Vellmar</p>
        <p class="brand-tagline">Jewelry &amp; Design Studio</p>
      </div>
    </section>
  </main>
</body>
</html>
```